Update New Business Card - For Start Up

I need to update my business card, I have our old version for example. I would like to keep to the same colors and theme. We are a threat reporting and case management tool for corporations and educational institutions.

Target Market(s)

Corporate Security and Human Resources, School Administrators and Superintendents.

Industry/Entity Type

Physical Security and Technology.

Contact Information for Business Card

My Name, Founder/CEO, phone number 555-214-6082, Logo, Web...

Colors
0054AA
0677BA
7BADD7
CADEEF
E8F1F8

Requirements
Must have
• Something new and trendy.

```html
<!DOCTYPE html>
<html lang="en">
<head>
<meta charset="UTF-8">
<title>Dana Whitlock – Business Card</title>
<link rel="stylesheet" href="https://fonts.googleapis.com/css2?family=Montserrat:wght@500;600;700&display=swap">
<style>
  :root {
    --navy-blue: #0054aa;
    --brand-blue: #0677ba;
    --sky-blue: #7badd7;
    --mist-blue: #cadeef;
    --ice-blue: #e8f1f8;
    --card-bg: #f6f9fc;
    --ink-gray: #4a4f57;
    --name-gray: #3c4048;
    --white: #ffffff;
  }
  html, body {
    margin: 0;
    padding: 0;
    overflow: hidden;
    background: var(--card-bg);
  }
  .card {
    position: relative;
    width: 1200px;
    height: 720px;
    background: var(--card-bg);
    font-family: "Montserrat", sans-serif;
    overflow: hidden;
  }
  .brand-panel {
    position: absolute;
    left: 0;
    top: 0;
    width: 500px;
    height: 720px;
    background: linear-gradient(160deg, var(--brand-blue) 0%, var(--navy-blue) 100%);
    border-radius: 0 90px 90px 0;
  }
  .brand-accent {
    position: absolute;
    left: 0;
    bottom: 0;
    width: 500px;
    height: 12px;
    background: var(--sky-blue);
    border-radius: 0 0 90px 0;
  }
  .brand {
    position: absolute;
    left: 0;
    top: 0;
    width: 500px;
    height: 720px;
    display: flex;
    align-items: center;
    justify-content: center;
    gap: 20px;
  }
  .brand-dot {
    width: 56px;
    height: 56px;
    border-radius: 50%;
    background: var(--white);
  }
  .brand-name {
    font-weight: 700;
    font-size: 50px;
    letter-spacing: 1px;
    color: var(--white);
  }
  .identity {
    position: absolute;
    left: 590px;
    top: 112px;
  }
  .person-name {
    margin: 0;
    font-weight: 700;
    font-size: 56px;
    line-height: 60px;
    letter-spacing: 2px;
    color: var(--name-gray);
    text-transform: uppercase;
  }
  .person-title {
    margin: 14px 0 0;
    font-weight: 600;
    font-size: 24px;
    letter-spacing: 3px;
    color: var(--brand-blue);
    text-transform: uppercase;
  }
  .title-rule {
    width: 64px;
    height: 6px;
    margin-top: 22px;
    border-radius: 3px;
    background: var(--sky-blue);
  }
  .contact-list {
    position: absolute;
    left: 590px;
    top: 368px;
    margin: 0;
    padding: 0;
    list-style: none;
    color: var(--ink-gray);
    font-weight: 600;
    font-size: 25px;
    letter-spacing: 1px;
  }
  .contact-item {
    display: flex;
    align-items: center;
    gap: 24px;
    margin-bottom: 26px;
  }
  .contact-chip {
    flex: none;
    width: 56px;
    height: 56px;
    border-radius: 16px;
    background: var(--mist-blue);
    display: flex;
    align-items: center;
    justify-content: center;
  }
  .contact-chip svg {
    width: 28px;
    height: 28px;
  }
  .contact-text {
    line-height: 32px;
  }
</style>
</head>
<body>
<div class="card">
  <div class="brand-panel"></div>
  <div class="brand-accent"></div>
  <div class="brand">
    <div class="brand-dot"></div>
    <div class="brand-name">Vantaro</div>
  </div>

  <div class="identity">
    <h1 class="person-name">Dana<br>Whitlock</h1>
    <p class="person-title">Founder / CEO</p>
    <div class="title-rule"></div>
  </div>

  <ul class="contact-list">
    <li class="contact-item">
      <span class="contact-chip">
        <svg viewBox="0 0 40 40" aria-hidden="true">
          <path d="M9 5c2-1 3 0 4 1l4 6c1 2 0 3-1 4l-2 2c1 3 5 8 9 9l2-2c1-1 2-2 4-1l6 4c1 1 2 2 1 4l-2 3c-1 1-3 2-5 1C17 33 7 23 6 11c-1-2 0-4 1-5z" fill="var(--navy-blue)"/>
        </svg>
      </span>
      <span class="contact-text">888-899-3799<br>555-214-6082</span>
    </li>
    <li class="contact-item">
      <span class="contact-chip">
        <svg viewBox="0 0 40 40" aria-hidden="true">
          <rect x="3" y="9" width="34" height="22" rx="3" fill="none" stroke="var(--navy-blue)" stroke-width="3"/>
          <polyline points="4,10 20,22 36,10" fill="none" stroke="var(--navy-blue)" stroke-width="3"/>
        </svg>
      </span>
      <span class="contact-text">dana@vantaro.co</span>
    </li>
    <li class="contact-item">
      <span class="contact-chip">
        <svg viewBox="0 0 40 40" aria-hidden="true">
          <g fill="none" stroke="var(--navy-blue)" stroke-width="2.6">
            <circle cx="20" cy="20" r="16"/>
            <ellipse cx="20" cy="20" rx="7" ry="16"/>
            <line x1="4" y1="20" x2="36" y2="20"/>
          </g>
        </svg>
      </span>
      <span class="contact-text">www.vantaro.co</span>
    </li>
  </ul>
</div>
</body>
</html>
```